Willowmere Spa and Beauty Ltd. (Name of business)

I need a business card designed for this new company based out of Toronto Ontario. We specialize in Eyelash Extensions, Manicures and Pedicures, body waxing, massages, laser hair removal and botox treatments. Also offer a variety of products for sale, such as skin cream serums, collagen gel, eye cream, etc. It is a safe relaxing and non-judgemental environnment. Clients are welcome to come be pampered for the half or full day. Many service packages to choose from.

Open 7days per week from 8am to 8pm.

Priscilla Dunmore
Spa Facilitator
Willowmere Spa and Beauty Ltd.
7200 Harcourt St; Suite 1400
Toronto ON K2P 9W4

OFFICE: 416.790.4100
FAX: 416.790.4101
CELL: 416.632.1987
EMAIL: priscilla.dunmore@willowmerespa.com

Target Market(s)

Target market is primarily female ranging from 16 years old to 50 years old.

Industry/Entity Type

Business

Contact Information for Business Card

Priscilla Dunmore
Spa Facilitator
7200 Harcourt St; Suite 1400
Toronto ON K2P 9W4

OFFICE: 416.790.4100
FAX: 416.790.4101
CELL: 416.632.1987

Logo Text

I dont have a logo yet. I would like it simple but sophisticated and modern.

Font styles to use
Serif

Requirements
Must have
• all pertinent details such as company name, logo, name and contact information, services that are offered, including package rates
Nice to have
• Company name and logo prominent. A card that is neat and the information such as address, phone number, fax, email, etc is not too crowded but laid out in an easy to read format.
• Possibly on the back of card - some of the services offered could be listed, as well as professional cream lotions and serums. Hours of operation etc.

```html
<!DOCTYPE html>
<html lang="en">
<head>
<meta charset="utf-8">
<title>Willowmere Spa and Beauty Ltd. — Business Card</title>
<link rel="stylesheet" href="https://fonts.googleapis.com/css2?family=Lora:ital,wght@0,400;0,600;0,700;1,400&display=swap">
<style>
  :root {
    --page-bg: #ece8ee;
    --card-white: #ffffff;
    --plum-deep: #6e1f86;
    --plum: #8a2c9e;
    --violet-soft: #8b63b6;
    --lavender: #c9a9dc;
    --lavender-pale: #e3d3ec;
    --hours-blue: #b7c6ff;
    --text-light: #f6eefa;
    --card-radius: 26px;
  }
  * { box-sizing: border-box; margin: 0; padding: 0; }
  html, body { width: 1200px; height: 900px; overflow: hidden; }
  body {
    background: var(--page-bg);
    font-family: "Lora", Georgia, serif;
    position: relative;
  }
  .card {
    position: absolute;
    left: 250px;
    width: 700px;
    height: 400px;
    border-radius: var(--card-radius);
    overflow: hidden;
    box-shadow: 0 10px 28px rgba(60, 20, 80, 0.22);
  }
  .card--front { top: 40px; background: var(--card-white); }
  .card--back {
    top: 465px;
    background: radial-gradient(ellipse at 55% 40%, #8d5fb8 0%, #7a2f9a 45%, #6a1d84 100%);
    color: var(--text-light);
  }
  .front-wave { position: absolute; inset: 0; width: 100%; height: 100%; }

  .brand { position: absolute; display: flex; align-items: center; gap: 14px; }
  .brand__dot { width: 26px; height: 26px; border-radius: 50%; flex: none; }
  .brand__name { font-size: 40px; font-weight: 400; line-height: 1; }
  .brand__tag { font-size: 17px; line-height: 1; margin-top: 6px; text-align: right; }
  .brand--front { top: 42px; right: 130px; color: var(--plum); }
  .brand--front .brand__dot { background: var(--violet-soft); }
  .brand--front .brand__tag { color: var(--violet-soft); }

  .person { position: absolute; left: 40px; top: 128px; }
  .person__name { font-size: 27px; font-weight: 700; color: var(--plum-deep); line-height: 1.25; }
  .person__role { font-size: 16px; color: var(--violet-soft); margin: 4px 0 12px; }
  .contact-list { list-style: none; font-size: 14px; color: var(--plum-deep); }
  .contact-list li { display: flex; align-items: center; gap: 9px; line-height: 21px; }
  .contact-list svg { width: 13px; height: 13px; fill: var(--plum-deep); flex: none; }

  .location { position: absolute; left: 398px; bottom: 30px; color: var(--text-light); font-size: 15px; line-height: 22px; font-style: normal; }
  .hours { margin-top: 10px; font-size: 13.5px; color: var(--hours-blue); text-transform: uppercase; white-space: nowrap; }

  .back-content { position: absolute; inset: 0; display: flex; flex-direction: column; align-items: center; justify-content: center; text-align: center; padding: 0 40px; }
  .brand--back { position: static; color: var(--text-light); margin-bottom: 22px; }
  .brand--back .brand__dot { background: var(--text-light); }
  .section-title { font-size: 19px; font-weight: 700; margin-top: 6px; }
  .offer-list { font-size: 15px; font-style: italic; line-height: 23px; color: var(--lavender-pale); }
</style>
</head>
<body>

<section class="card card--front" aria-label="Business card front">
  <svg class="front-wave" viewBox="0 0 700 400" preserveAspectRatio="none" aria-hidden="true">
    <defs>
      <linearGradient id="waveFill" x1="0" y1="1" x2="1" y2="0">
        <stop offset="0" stop-color="#74208c"/>
        <stop offset="0.6" stop-color="#8a52b0"/>
        <stop offset="1" stop-color="#9c3aa8"/>
      </linearGradient>
    </defs>
    <path d="M248 400 C 290 290, 400 245, 540 215 C 620 198, 670 160, 700 110 L700 400 Z" fill="#e3d3ec"/>
    <path d="M240 400 C 285 295, 395 258, 540 232 C 620 218, 672 180, 700 135 L700 400 Z" fill="#c9a9dc"/>
    <path d="M262 400 C 300 305, 405 272, 545 252 C 625 240, 675 205, 700 165 L700 400 Z" fill="url(#waveFill)"/>
    <path d="M560 190 C 620 175, 670 140, 700 60 L700 95 C 670 160, 620 185, 560 190 Z" fill="#b478c8"/>
  </svg>

  <div class="brand brand--front">
    <span class="brand__dot"></span>
    <div>
      <div class="brand__name">Willowmere Spa</div>
      <div class="brand__tag">And Beauty Ltd</div>
    </div>
  </div>

  <div class="person">
    <h1 class="person__name">Priscilla Dunmore</h1>
    <p class="person__role">Spa Facilitator</p>
    <ul class="contact-list">
      <li><svg viewBox="0 0 16 16"><path d="M3 1l3 0 1.5 4-2 1.5a9 9 0 0 0 4 4l1.5-2 4 1.5 0 3c0 1-1 2-2 2A13 13 0 0 1 1 3c0-1 1-2 2-2z"/></svg>416.790.4100</li>
      <li><svg viewBox="0 0 16 16"><path d="M4 1h7v4H4zM1 6h14v7h-3v2H4v-2H1zM5 10v4h6v-4z"/></svg>416.790.4101</li>
      <li><svg viewBox="0 0 16 16"><path d="M4 0h8a1 1 0 0 1 1 1v14a1 1 0 0 1-1 1H4a1 1 0 0 1-1-1V1a1 1 0 0 1 1-1zm1 2v10h6V2z"/></svg>416.632.1987</li>
      <li><svg viewBox="0 0 16 16"><path d="M1 3h14v10H1zm1.5 1.5L8 9l5.5-4.5z"/></svg>priscilla.dunmore@willowmerespa.com</li>
    </ul>
  </div>

  <address class="location">
    7200 Harcourt St; Suite 1400<br>
    Toronto ON K2P 9W4
    <p class="hours">Open 7days per week from 8am to 8pm.</p>
  </address>
</section>

<section class="card card--back" aria-label="Business card back">
  <div class="back-content">
    <div class="brand brand--back">
      <span class="brand__dot"></span>
      <div>
        <div class="brand__name">Willowmere Spa</div>
        <div class="brand__tag">And Beauty Ltd</div>
      </div>
    </div>
    <h2 class="section-title">Services</h2>
    <p class="offer-list">Eyelash Extensions | Manicures and Pedicures | body waxing massages<br>laser hair removal | botox treatments</p>
    <h2 class="section-title">Products for sale</h2>
    <p class="offer-list">skin cream serums | collagen gel | eye cream, etc.</p>
  </div>
</section>

</body>
</html>
```